BRIGHTDESK - Remote Tech Support Site

We are looking for a new very responsive and simple website for our brand Brightdesk.example - a remote technical support company.

This company supports customers Globally in different countries throughout Eur/ North America / South America / Asia etc (please keep this in mind and integrate into the idea).

Its important to us that the design is very explanatory, the customer should easily be able to figure out that we provide computer support right away ... I like one page responsive type designs as well without a bunch of menu items

Here are some similar sites we like - but still looking for a unique design that fits out brand "brightdesk" - I have upload also some layouts i like (but the designs are not important just the layouts), youll see it includes consumer business etc which is important.

PLOVE.EXAMPLE - I love how clean it is - nice and white easy to see everything

ZENBYTE247.EXAMPLE - also nice the layout and responsive one page design makes it easy to use

lumacorefix.example - similar to zenbyte design as well - you can get the idea im looking for between the two

You will notice those examples are much different then the attachments I added - again this is more of an idea for possible layouts .. attached is also the logo - could inspire color scheme / blue white black etc

Target Market(s)

Home consumers without computer knowledge , older age 45-65, small medium business ... computer repair - slow computers

Industry/Entity Type

Computer Repair

Logo Text

Brightdesk

Coding

Coded - Design and coding required

Number of Pages Required

1 page

Font styles to use
Sans Serif
Other font styles liked:
• your choice responsive

Colors

Designer to choose colors to be used in the design.

Requirements
Must have
• Clean - responsive - professional design - the name says it all - brightdesk
• CALL TO ACTIONS FOR "Get Help Now!" / "Learn More" etc
Nice to have
• We are looking for a new very responsive and simple website for our brand Brightdesk.example - a remote technical support company.
• This company supports customers Globally in different countries throughout Eur/ North America / South America / Asia etc (please keep this in mind and integrate into the idea).
• Its important to us that the design is very explanatory, the customer should easily be able to figure out that we provide computer support right away ... I like one page responsive type designs as well without a bunch of menu items
• Here are some similar sites we like - but still looking for a unique design that fits out brand "brightdesk" - I have upload also some layouts i like (but the designs are not important just the layouts), youll see it includes consumer business etc which is important.
• PLOVE.EXAMPLE - I love how clean it is - nice and white easy to see everything
• ZENBYTE247.EXAMPLE - also nice the layout and responsive one page design makes it easy to use
• lumacorefix.example - similar to zenbyte design as well - you can get the idea im looking for between the two
Should not have
• dark, packed page - bad small font -

```html
<!DOCTYPE html>
<html lang="en">
<head>
<meta charset="utf-8">
<title>Brightdesk – Remote Tech Support</title>
<link href="https://fonts.googleapis.com/css2?family=Roboto:wght@300;400;500;700;900&display=swap" rel="stylesheet">
<style>
:root{
  --blue:#1d8ee6;
  --blue-dark:#1474c2;
  --green:#5cb531;
  --green-dark:#4a9a25;
  --ink:#2b2b2b;
  --text:#555;
  --muted:#888;
  --line:#e3e3e3;
  --soft:#f4f5f7;
  --footer:#2a2a2a;
  --white:#fff;
}
*{margin:0;padding:0;box-sizing:border-box}
html,body{width:1200px;height:4986px;overflow:hidden}
body{font-family:"Roboto",Arial,sans-serif;color:var(--text);background:var(--white);font-size:14px;line-height:1.55}
section,header,footer{position:relative;width:1200px;overflow:hidden}
.abs{position:absolute}
.btn{display:inline-block;font-weight:500;text-transform:uppercase;font-size:13px;letter-spacing:.5px;border-radius:3px;padding:0 22px;line-height:40px;text-decoration:none}
.btn-blue{background:var(--blue);color:var(--white)}
.btn-green{background:var(--green);color:var(--white)}
.btn-outline{border:2px solid var(--ink);color:var(--ink);line-height:36px}
.photo{position:absolute}
.lorem{font-size:13px;line-height:1.6;color:var(--text)}

/* hero */
.hero{height:680px;background:linear-gradient(180deg,#fafbfc,#eef1f4)}
.topbar{position:absolute;left:0;top:0;width:1200px;height:33px;background:#3c3c3c;color:#ddd;font-size:12px}
.topbar .mail{left:160px;top:8px}
.topbar .lang{left:900px;top:7px;width:56px;height:18px;background:#555;border-radius:2px}
.topbar .login{left:990px;top:8px}
.hero-photo{left:500px;top:33px;width:700px;height:532px;background:linear-gradient(120deg,#e9edf1 0%,#cfd7df 45%,#b8c3cc 100%)}
.nav{left:0;top:33px;width:1200px;height:60px}
.logo{left:160px;top:12px;display:flex;align-items:center;gap:10px;font-size:26px;font-weight:700;color:var(--blue)}
.logo i{width:30px;height:30px;border-radius:50%;background:var(--blue);display:block}
.menu{left:500px;top:20px;display:flex;gap:26px;font-size:13px;font-weight:500;color:var(--white);background:rgba(40,40,40,.55);padding:4px 16px;border-radius:2px}
.phone{left:935px;top:14px;font-size:24px;font-weight:700;color:var(--ink);display:flex;align-items:center;gap:8px}
.hero h1{left:160px;top:150px;font-size:44px;line-height:1.1;font-weight:500;color:var(--blue)}
.hero h1 span{display:block;font-weight:300}
.checks{left:160px;top:280px;width:360px;display:grid;grid-template-columns:1fr 1fr;gap:10px 20px;font-size:12px;color:var(--ink);list-style:none}
.checks li{display:flex;align-items:center;gap:6px}
.checks li::before{content:"";width:8px;height:8px;border-radius:50%;background:var(--blue)}
.hero .cta{left:160px;top:375px}
.member{left:160px;top:572px;width:877px;height:86px;background:var(--white);box-shadow:0 3px 12px rgba(0,0,0,.12);display:flex;align-items:center}
.member .badge{width:150px;height:86px;background:var(--green);clip-path:polygon(0 0,100% 0,82% 100%,0 100%);display:flex;align-items:center;justify-content:center}
.member h3{font-size:24px;font-weight:700;color:var(--ink);margin-left:20px}
.member p{font-size:11px;color:var(--muted);margin-left:20px}
.member .btn{margin-left:auto;margin-right:20px}

/* how */
.how{height:425px;text-align:center}
.sec-title{font-size:32px;font-weight:700;color:var(--ink)}
.how .sec-title{margin-top:30px}
.how .intro{width:780px;margin:14px auto 0;font-size:12px}
.steps{display:flex;justify-content:center;gap:70px;margin-top:26px}
.step{width:230px}
.step .ic{width:74px;height:74px;border:3px solid var(--blue);border-radius:50%;margin:0 auto 12px;display:flex;align-items:center;justify-content:center}
.step h4{font-size:17px;font-weight:500;color:var(--ink);margin-bottom:6px}
.step p{font-size:12px}
.how .btn{margin-top:22px}

/* about */
.about{height:495px;background:var(--soft)}
.about-photo{left:0;top:0;width:615px;height:495px;background:linear-gradient(135deg,#cfd5da,#9ea8b2 60%,#6e7882)}
.about .txt{left:648px;top:60px;width:390px}
.about h2{font-size:34px;font-weight:700;color:var(--ink);margin-bottom:14px}
.about .lorem{font-size:12.5px;margin-bottom:14px}
.about .foot{display:flex;align-items:center;gap:30px;margin-top:18px}
.about .mini-logo{display:flex;align-items:center;gap:8px;font-size:26px;font-weight:700;color:var(--ink)}
.about .mini-logo i{width:28px;height:28px;border-radius:50%;background:var(--blue);display:block}

/* band */
.band{height:175px;background:var(--blue);text-align:center;color:var(--white)}
.band h2{font-size:34px;font-weight:500;margin-top:30px}
.band p{font-size:18px;font-weight:300;opacity:.9}
.band .btn{margin-top:16px;border:2px solid var(--white);color:var(--white);line-height:32px}

/* products */
.products{height:495px;text-align:center;background:var(--white)}
.products .sec-title{margin-top:30px;font-weight:500}
.cards{display:flex;gap:22px;margin:26px 0 0 160px}
.card{width:210px}
.card .img{height:232px;border:4px solid #e8e8e8;background:linear-gradient(135deg,#6fae4f,#2f6e8f)}
.card:nth-child(2) .img{background:linear-gradient(135deg,#4a4f5a,#a7acb3)}
.card:nth-child(3) .img{background:linear-gradient(135deg,#9fc6e6,#e8d07a)}
.card:nth-child(4) .img{background:linear-gradient(135deg,#1f5f9c,#7fb6e2)}
.card p{font-size:12px;margin-top:10px}
.card .price{font-size:22px;font-weight:500;color:var(--ink)}
.card .row{display:flex;justify-content:space-between;margin-top:10px}
.card .row .btn{font-size:11px;line-height:28px;padding:0 16px;text-transform:none}

/* realtime */
.realtime{height:475px;background:var(--soft)}
.rt-photo{left:0;top:0;width:615px;height:475px;background:linear-gradient(135deg,#d7c7b4,#9c8a76 55%,#5f5448)}
.rt-txt{left:642px;top:60px}
.rt-txt h2{font-size:46px;font-weight:900;color:var(--ink);line-height:1.05}
.rt-txt .sub{font-size:30px;font-weight:300;color:var(--ink);line-height:1.2}
.rt-txt .acc{font-size:42px;font-weight:700;color:var(--green);line-height:1.1}
.rt-list{list-style:none;margin:18px 0 24px;font-size:13px;color:var(--text)}
.rt-list li{display:flex;align-items:center;gap:10px;line-height:30px}

/* features */
.features{height:500px;background:linear-gradient(90deg,#e9ecef,#d8dde2)}
.feat-photo{left:640px;top:0;width:560px;height:500px;background:linear-gradient(135deg,#eaeef1,#c7ccd2 60%,#9aa3ad)}
.feat-panel{left:160px;top:0;width:621px;height:500px;background:rgba(92,181,49,.93);color:var(--white);text-align:center;padding-top:26px}
.feat-panel h2{font-size:38px;font-weight:700;line-height:1.1}
.feat-panel h3{font-size:20px;font-weight:400}
.feat-grid{display:grid;grid-template-columns:repeat(3,1fr);gap:22px 10px;padding:26px 30px 0}
.feat .ic{width:54px;height:54px;border-radius:50%;background:rgba(255,255,255,.2);margin:0 auto 8px;display:flex;align-items:center;justify-content:center}
.feat h4{font-size:13px;font-weight:700;text-transform:uppercase}
.feat p{font-size:10.5px;line-height:1.4;opacity:.9;padding:0 14px}
.feat-panel .btn{margin-top:20px;background:var(--white);color:var(--ink);line-height:34px}

/* pricing */
.pricing{height:625px;text-align:center}
.pricing .sec-title{margin-top:45px;font-size:28px}
.pricing .sec-title span{color:var(--green)}
.plan{position:absolute;background:var(--white);box-shadow:0 2px 10px rgba(0,0,0,.12)}
.plan .head{background:var(--blue);color:var(--white);font-size:20px;font-weight:700;line-height:68px}
.plan .price{font-size:46px;font-weight:700;color:var(--ink);margin-top:22px;line-height:1}
.plan .price sup{font-size:20px;vertical-align:top}
.plan .price small{font-size:13px;font-weight:500}
.plan .setup{font-size:12px;color:var(--muted)}
.plan .desc{background:#ececec;margin:22px 0 0;padding:18px 10px;font-size:12px}
.plan .desc b{display:block;color:var(--ink);font-size:13px}
.plan .pill{display:inline-flex;align-items:center;gap:10px;margin-top:26px;background:var(--blue);color:var(--white);border-radius:22px;padding:0 8px 0 24px;line-height:40px;font-size:13px;font-weight:700}
.plan .pill i{width:28px;height:28px;border-radius:50%;background:var(--white);display:block}
.p1{left:160px;top:152px;width:289px;height:426px}
.p2{left:449px;top:122px;width:309px;height:483px;z-index:2}
.p2 .head{background:var(--green);line-height:78px}
.p2 .pill{background:var(--green)}
.p3{left:758px;top:152px;width:279px;height:426px}

/* testimonial */
.testi{height:360px}
.quote{left:160px;top:26px;width:877px;height:186px;border:1px solid var(--line);box-shadow:0 1px 6px rgba(0,0,0,.06)}
.quote .pic{left:0;top:0;width:190px;height:186px;background:linear-gradient(135deg,#c9ced3,#7d8792)}
.quote .name{left:220px;top:16px;display:flex;align-items:center;gap:8px;font-size:18px;font-weight:500;color:var(--ink)}
.quote .name i{width:18px;height:18px;background:var(--blue);display:block;border-radius:2px}
.quote .stars{left:220px;top:44px;color:#f2b01e;font-size:13px;letter-spacing:2px}
.quote p{left:220px;top:64px;width:620px;font-size:12px}
.quote .more{left:220px;top:158px;font-size:11px;color:var(--blue)}
.partners{left:160px;top:245px;width:877px;display:flex;justify-content:space-between;align-items:center}
.partners span{font-size:24px;font-weight:500;color:#6a6a6a;width:160px;text-align:center;border:1px solid var(--line);line-height:80px;white-space:nowrap}

/* cta */
.cta-sec{height:350px;background:linear-gradient(120deg,var(--green),var(--green-dark))}
.video{left:160px;top:41px;width:405px;height:276px;border:6px solid var(--white);background:linear-gradient(135deg,#d5d9dd,#8f98a2)}
.cta-txt{left:700px;top:56px;color:var(--white)}
.cta-txt h2{font-size:32px;font-weight:700}
.cta-txt h3{font-size:26px;font-weight:300;line-height:1.25;width:360px}
.cta-txt small{display:block;font-size:12px;margin:8px 0 18px 50px;opacity:.9}
.cta-txt .btn{background:var(--white);color:var(--ink);display:inline-flex;align-items:center;gap:8px;margin-left:50px}

/* footer */
.site-footer{height:406px;background:var(--footer);color:#aaa;font-size:12px}
.f-col{position:absolute;top:40px}
.f-col h5{font-size:18px;font-weight:400;color:var(--white);margin-bottom:14px}
.f-col ul{list-style:none;line-height:26px}
.f-logo{display:flex;align-items:center;gap:8px;font-size:24px;font-weight:700;color:var(--white);margin-bottom:12px}
.f-logo i{width:26px;height:26px;border-radius:50%;background:var(--blue);display:block}
.social{display:flex;gap:8px;margin-top:10px}
.social i{width:22px;height:22px;border-radius:50%;background:#444;display:block}
.news{left:160px;top:270px}
.news h5{font-size:16px;color:var(--white);font-weight:400;margin-bottom:12px}
.news .field{display:flex}
.news .input{width:306px;height:40px;background:#444;color:#888;padding:0 12px;line-height:40px}
.news .btn{border-radius:0;margin-left:4px;text-transform:none;font-size:15px;padding:0 30px}
.trust{left:690px;top:270px}
.trust h5{font-size:16px;color:var(--white);font-weight:400;margin-bottom:12px}
.trust .row{display:flex;gap:18px;align-items:center}
.trust .circle{width:70px;height:70px;border-radius:50%;background:#666}
.trust .box{width:110px;height:48px;background:#555;border-radius:4px}
</style>
</head>
<body>

<header class="hero">
  <div class="topbar">
    <span class="abs mail">info@brightdesk.example</span>
    <span class="abs lang"></span>
    <span class="abs login">Login</span>
  </div>
  <div class="photo hero-photo" role="img" aria-label="Older couple smiling while using a laptop at home"></div>
  <nav class="abs nav">
    <div class="abs logo"><i></i>brightdesk</div>
    <div class="abs menu"><span>HOME</span><span>ABOUT US</span><span>SERVICES</span><span>CONTACT US</span></div>
    <div class="abs phone">
      <svg width="20" height="20" viewBox="0 0 24 24"><path fill="#2b2b2b" d="M6.6 10.8a15 15 0 0 0 6.6 6.6l2.2-2.2c.3-.3.7-.4 1-.2 1.1.4 2.3.6 3.6.6.6 0 1 .4 1 1V20c0 .6-.4 1-1 1C10.6 21 3 13.4 3 4c0-.6.4-1 1-1h3.5c.6 0 1 .4 1 1 0 1.3.2 2.5.6 3.6.1.3 0 .7-.2 1z"/></svg>
      (800) 555-0142
    </div>
  </nav>
  <h1 class="abs">Dedicated Support <span>Anytime.Anywhere.</span></h1>
  <ul class="abs checks">
    <li>Real Virus Optimization</li><li>Free Diagnostic</li>
    <li>Unlimited Cloud Backup</li><li>Leading Security Software</li>
  </ul>
  <a class="abs btn btn-blue cta">Get FREE PC help now</a>
  <div class="abs member">
    <div class="badge">
      <svg width="60" height="40" viewBox="0 0 60 40" fill="#fff"><circle cx="30" cy="11" r="8"/><path d="M16 38c0-9 6-14 14-14s14 5 14 14z"/><circle cx="12" cy="15" r="6"/><path d="M1 36c0-7 5-11 11-11 2 0 4 .5 5 1.5-3 3-4 6-4 9.5z"/><circle cx="48" cy="15" r="6"/><path d="M59 36c0-7-5-11-11-11-2 0-4 .5-5 1.5 3 3 4 6 4 9.5z"/></svg>
    </div>
    <div><h3>BECOME A MEMBER TODAY!</h3><p>Lorem ipsum is simply dummy text of the printing and typesetting industry.</p></div>
    <a class="btn btn-green">GET IT NOW ›</a>
  </div>
</header>

<section class="how">
  <h2 class="sec-title">HOW IT WORKS</h2>
  <p class="intro">Lorem Ipsum is simply dummy text of the printing and typesetting industry. Lorem Ipsum has been the industry's standard dummy text ever since, when an unknown printer took a galley of type and scrambled it to make a type specimen book.</p>
  <div class="steps">
    <div class="step">
      <div class="ic"><svg width="36" height="36" viewBox="0 0 24 24" fill="none" stroke="#1d8ee6" stroke-width="2"><rect x="3" y="4" width="18" height="12" rx="1"/><path d="M8 20h8M12 16v4"/></svg></div>
      <h4>FREE Diagnostic</h4>
      <p>Lorem Ipsum is simply dummy text of the printing and typesetting industry. Lorem Ipsum has been the industry's standard dummy text ever since.</p>
    </div>
    <div class="step">
      <div class="ic"><svg width="36" height="36" viewBox="0 0 24 24" fill="none" stroke="#1d8ee6" stroke-width="2"><circle cx="12" cy="12" r="8"/><path d="M8 12l3 3 5-6"/></svg></div>
      <h4>Get Fixed</h4>
      <p>Lorem Ipsum is simply dummy text of the printing and typesetting industry. Lorem Ipsum has been the industry's standard dummy text ever since.</p>
    </div>
    <div class="step">
      <div class="ic"><svg width="36" height="36" viewBox="0 0 24 24" fill="none" stroke="#1d8ee6" stroke-width="2"><path d="M7 18a5 5 0 0 1 0-10 6 6 0 0 1 11 2 4 4 0 0 1-1 8z"/><path d="M12 11v6M9 14l3 3 3-3"/></svg></div>
      <h4>Backup your information!</h4>
      <p>Lorem Ipsum is simply dummy text of the printing and typesetting industry. Lorem Ipsum has been the industry's standard dummy text ever since.</p>
    </div>
  </div>
  <a class="btn btn-outline">READ MORE ›</a>
</section>

<section class="about">
  <div class="photo about-photo" role="img" aria-label="Technician helping a colleague at a laptop in a bright office"></div>
  <div class="abs txt">
    <h2>ABOUT US</h2>
    <p class="lorem">Lorem Ipsum is simply dummy text of the printing and typesetting industry. Lorem Ipsum has been the industry's standard dummy text ever since the 1500s, when an unknown printer took a galley of type and scrambled it to make a type specimen book. It has survived not only five centuries, but also the leap into electronic typesetting, remaining essentially unchanged.</p>
    <p class="lorem">Lorem Ipsum is simply dummy text of the printing and typesetting industry. Lorem Ipsum has been the industry's standard dummy text ever since the 1500s, when an unknown printer took a galley of type and scrambled it to make a type specimen book.</p>
    <div class="foot"><a class="btn btn-outline">READ MORE ›</a><span class="mini-logo"><i></i>brightdesk</span></div>
  </div>
</section>

<section class="band">
  <h2>Computer Repair and IT Support Services</h2>
  <p>We're a 24/7, Cost Efficient Tech Repair Services for You</p>
  <a class="btn">CONTACT US</a>
</section>

<section class="products">
  <h2 class="sec-title">Our Products</h2>
  <div class="cards">
    <div class="card"><div class="img" role="img" aria-label="Laptop screen showing a protected status"></div><p>Lorem Ipsum simply dummy text</p><div class="price">$61.19</div><div class="row"><a class="btn btn-green">View more</a><a class="btn btn-blue">Add to cart</a></div></div>
    <div class="card"><div class="img" role="img" aria-label="Online security concept with keyboard"></div><p>Lorem Ipsum simply dummy text</p><div class="price">$61.19</div><div class="row"><a class="btn btn-green">View more</a><a class="btn btn-blue">Add to cart</a></div></div>
    <div class="card"><div class="img" role="img" aria-label="Data privacy concept with a padlock"></div><p>Lorem Ipsum simply dummy text</p><div class="price">$61.19</div><div class="row"><a class="btn btn-green">View more</a><a class="btn btn-blue">Add to cart</a></div></div>
    <div class="card"><div class="img" role="img" aria-label="Padlock on a blue digital circuit background"></div><p>Lorem Ipsum simply dummy text</p><div class="price">$61.19</div><div class="row"><a class="btn btn-green">View more</a><a class="btn btn-blue">Add to cart</a></div></div>
  </div>
</section>

<section class="realtime">
  <div class="photo rt-photo" role="img" aria-label="Family gathered around a laptop at home"></div>
  <div class="abs rt-txt">
    <h2>REAL-TIME</h2>
    <div class="sub">SUPPORT FEATURES AND</div>
    <div class="acc">BENEFITS</div>
    <ul class="rt-list">
      <li><svg width="14" height="14" viewBox="0 0 24 24"><path d="M4 12l5 5L20 6" fill="none" stroke="#5cb531" stroke-width="3"/></svg>24/7 Real-Time Technician Support</li>
      <li><svg width="14" height="14" viewBox="0 0 24 24"><path d="M4 12l5 5L20 6" fill="none" stroke="#5cb531" stroke-width="3"/></svg>The best Security Software on the market</li>
      <li><svg width="14" height="14" viewBox="0 0 24 24"><path d="M4 12l5 5L20 6" fill="none" stroke="#5cb531" stroke-width="3"/></svg>Regular tune-ups and optimization</li>
      <li><svg width="14" height="14" viewBox="0 0 24 24"><path d="M4 12l5 5L20 6" fill="none" stroke="#5cb531" stroke-width="3"/></svg>Setup and installation included</li>
    </ul>
    <a class="btn btn-blue">BECOME A MEMBER</a>
  </div>
</section>

<section class="features">
  <div class="photo feat-photo" role="img" aria-label="Smiling woman wearing a headset at a help desk"></div>
  <div class="abs feat-panel">
    <h2>ALL THE BEST FEATURES</h2>
    <h3>AT THE BEST PRICE!</h3>
    <div class="feat-grid">
      <div class="feat"><div class="ic"><svg width="26" height="26" viewBox="0 0 24 24" fill="none" stroke="#fff" stroke-width="2"><circle cx="12" cy="12" r="8"/><path d="M6 18L18 6"/></svg></div><h4>Ad Blocker</h4><p>Avoid unwanted pop-ups and ads while you browse.</p></div>
      <div class="feat"><div class="ic"><svg width="26" height="26" viewBox="0 0 24 24" fill="none" stroke="#fff" stroke-width="2"><circle cx="12" cy="12" r="3"/><circle cx="12" cy="12" r="8"/></svg></div><h4>Regular Tune-Ups</h4><p>Get a regular tune-up to keep your PC fast.</p></div>
      <div class="feat"><div class="ic"><svg width="26" height="26" viewBox="0 0 24 24" fill="none" stroke="#fff" stroke-width="2"><path d="M5 20V10M12 20V4M19 20v-7"/></svg></div><h4>System Reports</h4><p>Clear reports on the health of your system.</p></div>
      <div class="feat"><div class="ic"><svg width="26" height="26" viewBox="0 0 24 24" fill="none" stroke="#fff" stroke-width="2"><rect x="2" y="5" width="14" height="10"/><rect x="17" y="8" width="5" height="11"/></svg></div><h4>Multiple Devices</h4><p>One plan covers every device in your home.</p></div>
      <div class="feat"><div class="ic"><svg width="26" height="26" viewBox="0 0 24 24" fill="none" stroke="#fff" stroke-width="2"><rect x="7" y="2" width="10" height="20" rx="2"/></svg></div><h4>Mobile Security</h4><p>Keep your phone and tablet safe on the go.</p></div>
      <div class="feat"><div class="ic"><svg width="26" height="26" viewBox="0 0 24 24" fill="none" stroke="#fff" stroke-width="2"><path d="M7 18a5 5 0 0 1 0-10 6 6 0 0 1 11 2 4 4 0 0 1-1 8z"/></svg></div><h4>Cloud Backup</h4><p>Your files stored safely and always available.</p></div>
    </div>
    <a class="btn">VIEW MORE ›</a>
  </div>
</section>

<section class="pricing">
  <h2 class="sec-title">MEMBERSHIP PRICING <span>AND</span> PLANS</h2>
  <div class="plan p1">
    <div class="head">PREMIUM</div>
    <div class="price"><sup>$</sup>19.99<small>/MONTHLY</small></div>
    <div class="setup">($249-$300 setup fee)</div>
    <div class="desc">Regular 90 Day Optimization<b>Unlimited 24/7 Tier 3 Technician Support</b></div>
    <span class="pill">LEARN MORE <i></i></span>
  </div>
  <div class="plan p2">
    <div class="head">PREMIUM PLUS</div>
    <div class="price"><sup>$</sup>29.99<small>/MONTHLY</small></div>
    <div class="setup">($249-$300 setup fee)</div>
    <div class="desc">Regular 90 Day Optimization<b>Unlimited 24/7 Tier 3 Technician Support</b></div>
    <span class="pill">LEARN MORE <i></i></span>
  </div>
  <div class="plan p3">
    <div class="head">PLATINUM</div>
    <div class="price"><sup>$</sup>19.99<small>/MONTHLY</small></div>
    <div class="setup">($249-$300 setup fee)</div>
    <div class="desc">Regular 90 Day Optimization<b>Unlimited 24/7 Tier 3 Technician Support</b></div>
    <span class="pill">LEARN MORE <i></i></span>
  </div>
</section>

<section class="testi">
  <div class="abs quote">
    <div class="abs pic" role="img" aria-label="Portrait of a customer"></div>
    <div class="abs name"><i></i>Dana Whitfield</div>
    <div class="abs stars">★★★★★</div>
    <p class="abs">Lorem Ipsum is simply dummy text of the printing and typesetting industry. Lorem Ipsum has been the industry's standard dummy text ever since the 1500s, when an unknown printer took a galley of type and scrambled it to make a type specimen book. It has survived not only five centuries, but also the leap into electronic typesetting, remaining essentially unchanged.</p>
    <span class="abs more">Say More</span>
  </div>
  <div class="abs partners">
    <span>Fernmoor</span><span>Dalvane</span><span>Kestrane</span><span>Sornely</span><span>Tallow</span>
  </div>
</section>

<section class="cta-sec">
  <div class="photo video" role="img" aria-label="Video still of a smiling older man using a computer"></div>
  <div class="abs cta-txt">
    <h2>GET A 30-MINUTE ONE-ON-ONE</h2>
    <h3>FREE CONSULTATION WITH ONE OF OUR EXPERTS! *</h3>
    <small>*Limited period offer</small>
    <a class="btn"><svg width="14" height="14" viewBox="0 0 24 24"><path fill="#2b2b2b" d="M6.6 10.8a15 15 0 0 0 6.6 6.6l2.2-2.2c.3-.3.7-.4 1-.2 1.1.4 2.3.6 3.6.6.6 0 1 .4 1 1V20c0 .6-.4 1-1 1C10.6 21 3 13.4 3 4c0-.6.4-1 1-1h3.5c.6 0 1 .4 1 1 0 1.3.2 2.5.6 3.6.1.3 0 .7-.2 1z"/></svg>CALL US TODAY</a>
  </div>
</section>

<footer class="site-footer">
  <div class="f-col" style="left:160px;width:280px">
    <div class="f-logo"><i></i>brightdesk</div>
    <p>We are a group of technicians who work round the clock to ensure that your PC runs perfectly. Our team helps homes and small businesses.</p>
    <p style="margin-top:10px">Get in touch with us any time of day, from any country we serve.</p>
  </div>
  <div class="f-col" style="left:485px">
    <h5>Quick Links</h5>
    <ul><li>› Home</li><li>› About Us</li><li>› Services</li><li>› Contact Us</li><li>› FAQ</li></ul>
  </div>
  <div class="f-col" style="left:690px">
    <h5>Our Support</h5>
    <ul><li>Contact us</li><li>info@brightdesk.example</li><li>(800) 555-0142</li></ul>
    <div class="social"><i></i><i></i><i></i><i></i></div>
  </div>
  <div class="f-col" style="left:900px">
    <h5>Plans</h5>
    <ul><li>› Premium Plan</li><li>› Premium Plus</li><li>› Platinum Plan</li></ul>
  </div>
  <div class="abs news">
    <h5>Newsletter Signup</h5>
    <div class="field"><div class="input">Enter your email</div><a class="btn btn-blue">Sign up</a></div>
  </div>
  <div class="abs trust">
    <h5>Trusted By</h5>
    <div class="row"><span class="circle"></span><span class="circle"></span><span class="box"></span></div>
  </div>
</footer>

</body>
</html>
```